Cleaning Company and Staynest Tasks

Our London based company provides services for all things related to Staynest. Our main tasks are cleaning, checkins & linen. We are in need of a fresh new design that allows customers to book our services with ease.

The site must keep in mind that it will be primarily used on mobile and payment to be taken online.

What we require:

- Two pages designed, Home page (see Homepage doc) and Purchase Page (see flow chart)

Things we like:-

- We like mainly white and pastel based colours.
- Usage of vector style graphics through our the site to represent people & tasks.
- Shopping cart, with lots of images to select services
- Shopping cart that always has the pricing floating on the right
- Shopping cart that is wizard based.
- We like the usage of wonk characters on this site (for us probably angels)
http://www.tradelarks.com/pricing.php
- Slightly quirky design.

Sites we like:
http://vantageforge.com/ - bold action
https://www.mailorbit.com/ - a very playful design

TO AVOID WASTING TIME, INITIALLY DESIGN THE FRONT PAGE ONLY, IF WE LIKE YOUR HOME PAGE DESIGN THEM WE CAN SHORT LIST YOU INTO DESIGNING THE PAYMENT WIZARD PAGE

Target Market(s)

Young working professionals.

Industry/Entity Type

Cleaning Service

Contact Information for Business Card

Name: Rob Patel
Title: Senior Sales Representative
Tel: +44 (0) 777 4818 5096
Office: +44 (0) 207 413 6871
email: mh@fernhollowstays.co.uk
web: www.fernhollowstays.co.uk

Number of Pages Required

2 page

Font styles to use
Sans Serif

Colors
876aae
6b449b

Requirements
Must have
• - Two pages designed including home page and wizard to purchase services.
• - Usage of vector images.
Nice to have
• Angels to represent tasks
• We also like the colour yellow, the branding can be changed to suit this colour change.
Should not have
• A design that must not look like a Pagecraft standard Pagecraft theme.

```html
<!DOCTYPE html>
<html lang="en">
<head>
<meta charset="utf-8">
<title>Fernhollow – Book local housekeeping</title>
<link rel="stylesheet" href="https://fonts.googleapis.com/css2?family=Jost:wght@400;500&family=Roboto:wght@400;500&display=swap">
<style>
:root{
  --green:#86d400;
  --green-soft:#d9f2b0;
  --ink:#1d1d1d;
  --text:#333;
  --muted:#8a8a8a;
  --line:#dcdcdc;
  --field:#e3e3e3;
  --orange:#e89a1c;
  --dot:#cfcfcf;
  --white:#fff;
}
*{box-sizing:border-box;margin:0;padding:0}
h1,h2,h3,h4{font-weight:400}
html,body{width:1200px;height:2980px;overflow:hidden;background:var(--white)}
body{position:relative;font-family:"Roboto",Arial,sans-serif;color:var(--text)}
.abs{position:absolute}
.display{font-family:"Jost","Helvetica Neue",sans-serif}
.center{left:0;width:1200px;text-align:center}

/* header */
.site-header{position:absolute;left:0;top:0;width:1200px;height:90px;z-index:3}
.brand{display:flex;align-items:center;gap:12px;font-family:"Jost",sans-serif;font-weight:500;font-size:21px;letter-spacing:1px;color:var(--ink)}
.brand-dot{width:22px;height:22px;border-radius:50%;background:var(--green)}
.nav a{position:absolute;top:36px;font-size:12px;color:#444;text-decoration:none;letter-spacing:.3px}
.signin{left:1060px;top:26px;width:94px;height:36px;border:2px solid #9a9a9a;border-radius:3px;font-size:12px;font-weight:500;color:#444;display:flex;align-items:center;justify-content:center;background:rgba(255,255,255,.35)}

/* hero */
.hero-photo{left:480px;top:0;width:720px;height:672px;z-index:0;background:linear-gradient(90deg,#fff 0%,rgba(255,255,255,.6) 18%,rgba(255,255,255,0) 40%),linear-gradient(160deg,#f1f2f3 0%,#e4e6e8 45%,#c9c4bc 75%,#8f8f8a 100%)}
.hero-title{left:98px;top:148px;font-size:35px;line-height:44px;color:var(--ink)}
.hero-note{left:98px;top:268px;font-size:14px;color:#555}
.form-title{left:98px;top:324px;font-size:19px;color:var(--ink);font-weight:500}
.field{height:40px;border:1px solid var(--field);border-radius:2px;font-size:13px;color:#999;padding:0 14px;display:flex;align-items:center}
.btn{background:var(--green);color:var(--white);font-family:"Jost",sans-serif;font-weight:500;font-size:17px;display:flex;align-items:center;justify-content:center;letter-spacing:.3px}
.account{left:98px;width:378px;top:574px;text-align:center;font-size:14px;color:#444}
.account span{color:var(--green)}

/* sections */
.eyebrow{font-size:16px;color:var(--ink)}
.section-title{font-size:31px;color:var(--green)}
.rule{height:1px;background:var(--green);width:106px;left:547px}

.service-title{width:260px;text-align:center;font-family:"Jost",sans-serif;font-size:15px;letter-spacing:.5px;color:var(--ink)}
.service-list{list-style:none;font-size:12px;line-height:21px;color:#333}
.service-list li::before{content:"–";color:var(--green);margin-right:12px}
.icon{stroke:var(--green);fill:none;stroke-width:2.4;stroke-linejoin:round;stroke-linecap:round}

.why-title{width:368px;text-align:center;font-family:"Jost",sans-serif;font-size:19px;color:var(--ink)}
.why-text{width:368px;text-align:center;font-size:14px;line-height:23px;color:#222}
.vdivider{width:1px;height:160px;background:#e6e6e6;top:1420px}

.stars{color:var(--orange);font-size:22px;letter-spacing:3px}

.step-title{left:298px;top:1880px;font-family:"Jost",sans-serif;font-size:19px;color:var(--green)}
.step-text{left:298px;top:1912px;font-size:13px;line-height:18px;color:#111;width:270px}
.track{top:2003px;height:3px;background:#ddd;left:250px;width:698px}
.track-done{top:2003px;height:3px;background:var(--green);left:250px;width:350px}
.stop{width:18px;height:18px;border-radius:50%;background:var(--dot);top:1995px}

.quote{width:312px;font-size:14px;line-height:24px;color:#444}
.avatar{width:66px;height:66px;border-radius:50%;background:radial-gradient(circle at 50% 40%,#e7c4ad 0%,#b98670 55%,#6b4435 100%)}
.person{font-family:"Jost",sans-serif;font-size:15px;color:#555}
.person-meta{font-size:11px;line-height:15px;color:#999}

/* footer */
.hline{height:1px;background:#e4e4e4}
.foot-head{font-family:"Jost",sans-serif;font-size:19px;color:var(--ink)}
.foot-links{list-style:none;font-size:13px;line-height:18px;color:#888}
.copyright{font-size:10px;color:#bbb}
</style>
</head>
<body>

<section class="hero">
  <div class="abs hero-photo" role="img" aria-label="Photo of a bright white living room with plants, a guitar and a lamp"></div>
  <h1 class="abs hero-title display">Book local Housekeeping<br>professional at $59 / month</h1>
  <p class="abs hero-note">Currently operating in London and Cardiff Only.</p>
  <h2 class="abs form-title">Get Started Here</h2>
  <div class="abs field" style="left:98px;top:370px;width:284px">Home address</div>
  <div class="abs field" style="left:382px;top:370px;width:94px">Unit #</div>
  <div class="abs field" style="left:98px;top:418px;width:378px">Phone number</div>
  <div class="abs field" style="left:98px;top:468px;width:378px;justify-content:space-between">Select service type<span style="font-size:9px">▼</span></div>
  <div class="abs btn" style="left:98px;top:514px;width:378px;height:46px">BOOK NOW</div>
  <p class="abs account">Got an account? <span>Sign In</span></p>
</section>

<header class="site-header">
  <div class="abs brand" style="left:40px;top:30px"><span class="brand-dot"></span>FERNHOLLOW</div>
  <nav class="nav">
    <a href="#" style="left:672px">ABOUT</a>
    <a href="#" style="left:758px">APPLY AS A HOUSEKEEPER</a>
    <a href="#" style="left:958px">CONTACT</a>
  </nav>
  <div class="abs signin">SIGN IN</div>
</header>

<section class="services">
  <p class="abs center eyebrow" style="top:722px">No manual required</p>
  <h2 class="abs center section-title display" style="top:756px">Find a cleaner, pay online, relax</h2>
  <div class="abs rule" style="top:822px"></div>

  <svg class="abs" style="left:184px;top:900px" width="72" height="72" viewBox="0 0 72 72" aria-hidden="true">
    <path class="icon" d="M6 34 L36 8 L66 34 M14 28 V66 H58 V28 M26 66 V44 H38 V66 M44 42 H54 V52 H44 Z"/>
  </svg>
  <svg class="abs" style="left:448px;top:902px" width="70" height="70" viewBox="0 0 70 70" aria-hidden="true">
    <path class="icon" d="M4 4 H66 V66 H4 Z M10 10 H60 V60 H10 Z M35 10 V60 M10 35 H60 M18 26 L28 16 M42 52 L54 40"/>
  </svg>
  <svg class="abs" style="left:686px;top:898px" width="76" height="76" viewBox="0 0 76 76" aria-hidden="true">
    <path class="icon" d="M36 8 H54 L58 16 H40 M42 16 V26 M36 26 H54 L62 70 H28 Z M30 12 H6 M22 6 L10 4 M22 18 L10 20"/>
  </svg>
  <svg class="abs" style="left:944px;top:898px" width="80" height="76" viewBox="0 0 80 76" aria-hidden="true">
    <path class="icon" d="M40 4 V44 M18 60 C18 44 62 44 62 60 Z M8 64 H72 M14 54 C8 54 6 60 10 62 M66 54 C72 54 74 60 70 62"/>
  </svg>

  <h3 class="abs service-title" style="left:90px;top:996px">STAYNEST MANAGEMENT</h3>
  <h3 class="abs service-title" style="left:354px;top:996px">STAYNEST TASKS</h3>
  <h3 class="abs service-title" style="left:606px;top:996px">DOMESTIC CLEANING</h3>
  <h3 class="abs service-title" style="left:854px;top:996px">HANDYMAN</h3>

  <ul class="abs service-list" style="left:134px;top:1042px">
    <li>Lorem in</li><li>Lorem out</li><li>loreming</li><li>loremaphy</li><li>loreting lorting</li><li>Lorem Service</li>
  </ul>
  <ul class="abs service-list" style="left:432px;top:1042px">
    <li>Checkin</li><li>Check out</li><li>Cleaning</li><li>Photography</li><li>Listing Writing / Optimisation</li><li>Linen Service</li>
  </ul>
  <ul class="abs service-list" style="left:658px;top:1042px">
    <li>Lorem in</li><li>Lorem out</li><li>loreming</li><li>loremaphy</li><li>loreting lorting</li><li>Lorem Service</li>
  </ul>
  <ul class="abs service-list" style="left:940px;top:1042px">
    <li>Lorem in</li><li>Lorem out</li><li>loreming</li><li>loremaphy</li><li>loreting lorting</li><li>Lorem Service</li>
  </ul>
</section>

<section class="why">
  <h2 class="abs center section-title display" style="top:1256px">Why work with us</h2>
  <div class="abs rule" style="top:1324px"></div>

  <h3 class="abs why-title" style="left:46px;top:1422px">Trusted Professionals</h3>
  <h3 class="abs why-title" style="left:416px;top:1422px">Same-day Availability</h3>
  <h3 class="abs why-title" style="left:790px;top:1422px">Our Guarantee</h3>
  <div class="abs vdivider" style="left:424px"></div>
  <div class="abs vdivider" style="left:792px"></div>
  <p class="abs why-text" style="left:46px;top:1498px">Our own trusted vetted professionals.<br>They are all experienced, friendly,<br>background checked &amp; insured</p>
  <p class="abs why-text" style="left:416px;top:1498px">Book online it take a two minutes,<br>and schedule one of our team at<br>your place as early as the same day</p>
  <p class="abs why-text" style="left:790px;top:1498px">If you're not satisfied with our work,<br>we'll send an alternative cleaner<br>to re-do it for free</p>

  <p class="abs center" style="top:1638px;font-size:16px;color:var(--orange)">Best quality value for your money</p>
  <p class="abs center stars" style="top:1656px">★★★★★</p>
</section>

<section class="steps">
  <h2 class="abs center section-title display" style="top:1752px">How it works</h2>
  <div class="abs rule" style="top:1820px"></div>

  <svg class="abs" style="left:252px;top:1874px" width="30" height="24" viewBox="0 0 30 24" aria-hidden="true">
    <path d="M3 12 L11 20 L27 3" stroke="var(--green)" stroke-width="3.5" fill="none" stroke-linecap="round"/>
  </svg>
  <svg class="abs" style="left:228px;top:1900px" width="50" height="66" viewBox="0 0 50 66" aria-hidden="true">
    <path class="icon" d="M14 36 V8 C14 2 22 2 22 8 V30 M22 28 C22 22 30 22 30 28 M30 30 C30 24 38 24 38 30 M38 32 C38 26 46 26 46 32 V48 C46 58 40 62 30 62 H24 C16 62 12 56 6 44 C4 38 10 34 14 40"/>
  </svg>
  <h3 class="abs step-title">Select a service</h3>
  <p class="abs step-text">Lorem ipsum dolor sit amet,<br>aliquam natoque wisi vestibulum,<br>sodales sit nisl augue quia quis</p>

  <svg class="abs" style="left:562px;top:1906px" width="76" height="58" viewBox="0 0 76 58" aria-hidden="true">
    <g fill="none" stroke="#cdcdcd" stroke-width="2.4"><rect x="4" y="6" width="68" height="48" rx="3"/><path d="M18 2 V10 M58 2 V10"/><path d="M16 22 H60 M16 32 H60 M16 42 H60" stroke-dasharray="3 6"/><rect x="30" y="24" width="14" height="12"/></g>
  </svg>
  <svg class="abs" style="left:736px;top:1906px" width="74" height="56" viewBox="0 0 74 56" aria-hidden="true">
    <g fill="none" stroke="#cdcdcd" stroke-width="2.4"><rect x="4" y="4" width="60" height="38" rx="3"/><rect x="12" y="14" width="60" height="38" rx="3" fill="#fff"/><path d="M12 24 H72"/><circle cx="38" cy="38" r="5"/><circle cx="46" cy="38" r="5"/></g>
  </svg>
  <svg class="abs" style="left:914px;top:1880px" width="66" height="84" viewBox="0 0 66 84" aria-hidden="true">
    <g fill="none" stroke="#cdcdcd" stroke-width="2.4"><circle cx="33" cy="14" r="8"/><circle cx="20" cy="26" r="8"/><circle cx="46" cy="26" r="8"/><path d="M33 34 V50 M8 50 H58 L52 80 H14 Z"/></g>
  </svg>

  <div class="abs track"></div>
  <div class="abs track-done"></div>
  <div class="abs" style="left:236px;top:1990px;width:30px;height:30px;border-radius:50%;background:var(--green-soft)"></div>
  <div class="abs" style="left:242px;top:1996px;width:18px;height:18px;border-radius:50%;background:var(--green)"></div>
  <div class="abs stop" style="left:591px"></div>
  <div class="abs stop" style="left:763px"></div>
  <div class="abs stop" style="left:937px"></div>
</section>

<section class="testimonials">
  <h2 class="abs center section-title display" style="top:2082px">Testimonials</h2>
  <div class="abs rule" style="top:2150px"></div>

  <p class="abs quote" style="left:236px;top:2226px">I love that I can easily access and book online online my cleaning schedule and leave specific instructions for what I want the cleaner to focus on each day. Thank you for an amazing cleaning service !</p>
  <div class="abs avatar" style="left:236px;top:2364px" role="img" aria-label="Portrait photo of a customer"></div>
  <p class="abs person" style="left:320px;top:2374px">Lena M</p>
  <p class="abs person-meta" style="left:320px;top:2396px">San Francisco<br>Regular customer for 4 months</p>

  <p class="abs quote" style="left:656px;top:2226px">I love that I can easily access and book online online my cleaning schedule and leave specific instructions for what I want the cleaner to focus on each day. Thank you for an amazing cleaning service !</p>
  <div class="abs avatar" style="left:656px;top:2364px" role="img" aria-label="Portrait photo of a customer"></div>
  <p class="abs person" style="left:740px;top:2374px">Lena M</p>
  <p class="abs person-meta" style="left:740px;top:2396px">San Francisco<br>Regular customer for 4 months</p>

  <div class="abs btn" style="left:414px;top:2518px;width:378px;height:46px">BOOK NOW</div>
  <p class="abs center" style="top:2580px;font-size:16px;color:#333">Join our happy customers now</p>
</section>

<footer>
  <div class="abs hline" style="left:160px;top:2692px;width:880px"></div>
  <div class="abs brand" style="left:98px;top:2754px"><span class="brand-dot"></span>FERNHOLLOW</div>

  <h4 class="abs foot-head" style="left:556px;top:2756px">Company</h4>
  <ul class="abs foot-links" style="left:556px;top:2798px">
    <li>Pricing</li><li>Jobs</li><li>Terms and Conditions</li><li>Privacy Policy</li><li>Legal Notice</li>
  </ul>
  <h4 class="abs foot-head" style="left:768px;top:2756px">Features</h4>
  <ul class="abs foot-links" style="left:768px;top:2798px">
    <li>Search Services</li><li>Search Cleaners</li><li>Search Places</li>
  </ul>
  <h4 class="abs foot-head" style="left:982px;top:2756px">Help &amp; Support</h4>
  <ul class="abs foot-links" style="left:982px;top:2798px">
    <li>FAQ</li><li>Contact</li>
  </ul>

  <div class="abs hline" style="left:160px;top:2936px;width:880px"></div>
  <p class="abs center copyright" style="top:2954px">All rights reserved to Fernhollow LLC 2016. UK</p>
</footer>

</body>
</html>
```